Bright Thrift needs a web design and brand identifier

Bright Thrift is a pioneering approach by Victorian councils and four greenhouse alliances to support low income households to install solar systems with no upfront costs.

Bright Thrift will commence in May 2017.

Bright Thrift is looking for a designer to create a website banner incorporating a brand identifier for Bright Thrift. The brand identifier will be used in Bright Thrift promotional materials, such as flyers and mail outs.

The website banner and brand identifier should engender trust and confidence in the target group (retirees).
Updates

Reason: Hi, Thank you for your work so far. We've been given advice to get a separate logo designed (instead of trying to include this as part of the banner design). Sorry for not realising this until now - we're new to all this. So, I have a couple of preliminary logo designs that are being considered by our project control group. I will forward a copy of the logo once we have it. The project control group is looking for a web design that is unique to Bright Thrift and a design that draws on the key elements of the program (i.e. it helps people save money and take control). The site should be friendly but not too informal as the target group is seniors. Here's a link to another community energy organisation: www.kindlecurrent.com.au/ Apologies again for the delays. Cheers, Ned

Target Market(s)

Home owning, low income, retirees

Industry/Entity Type

Non Profit

Number of Pages Required

1 page

Font styles to use
Sans Serif

Requirements
Must have
• Use of Bright Thrift name
• Must promote Bright Thrift as safe, reliable and trustworthy
Nice to have
• Blue - to engender sense of safety and confidence (open to suggestions, though)
• Solar panels / the sun
Should not have
• Anything that is hard to read
• anything that promotes riskyness

```html
<!DOCTYPE html>
<html lang="en">
<head>
<meta charset="utf-8">
<title>Bright Thrift – Supports Pensioners</title>
<link rel="stylesheet" href="https://fonts.googleapis.com/css2?family=Open+Sans:wght@400;600;700&family=Oswald:wght@400;500&display=swap">
<style>
:root{
  --blue:#0b5aa8;
  --blue-dark:#0a3f7e;
  --blue-light:#1d74c6;
  --navy:#13294a;
  --ink:#222;
  --muted:#555;
  --grey-bg:#eceef0;
  --footer:#1c1d1f;
  --footer-text:#b8b8b8;
  --white:#fff;
}
*{box-sizing:border-box;margin:0;padding:0}
html,body{width:1200px;height:3051px;overflow:hidden}
body{font-family:"Open Sans",Arial,sans-serif;color:var(--ink);background:var(--white);position:relative}
.abs{position:absolute}

/* header */
.site-header{position:absolute;left:0;top:0;width:1200px;height:112px;background:var(--white)}
.topbar{position:absolute;left:722px;top:0;width:398px;height:33px;background:var(--blue);border-radius:0 0 0 18px;color:#fff;font-size:17px;display:flex;align-items:center}
.topbar .mail{padding-left:26px;display:flex;align-items:center;gap:10px;width:225px}
.topbar .phone{background:#111;height:33px;flex:1;display:flex;align-items:center;gap:10px;padding-left:18px;border-radius:0 0 16px 0}
.brand{position:absolute;left:80px;top:26px;display:flex;align-items:center;gap:14px}
.brand .mark{width:62px;height:62px;background:var(--blue)}
.brand .name{font-size:33px;font-weight:700;color:var(--blue);line-height:1}
.brand .sub{font-size:17px;font-weight:700;color:var(--blue);letter-spacing:.5px;margin-top:6px}
.main-nav{position:absolute;top:63px;left:478px;display:flex;gap:0;font-size:15px;font-weight:600}
.main-nav a{color:var(--ink);text-decoration:none;padding:5px 12px;margin-right:8px}
.main-nav a.active{background:var(--blue);color:#fff;border-radius:2px}

/* hero */
.hero{position:absolute;left:0;top:112px;width:1200px;height:580px;background:linear-gradient(180deg,#f4f5f6 0%,#d9dde2 45%,#5c636c 62%,#8c939c 80%,#c3c7cc 100%)}
.hero-panel{position:absolute;left:0;top:183px;width:627px;height:244px;background:rgba(40,40,40,.78)}
.hero-panel h1{font-family:"Oswald",Arial,sans-serif;font-weight:500;color:#fff;font-size:29px;line-height:47px;letter-spacing:.5px;position:absolute;left:84px;top:18px;text-transform:uppercase}
.btn-call{position:absolute;left:84px;top:157px;width:274px;height:58px;background:var(--blue);border:4px solid #9ab2cc;color:#fff;font-family:"Oswald",Arial,sans-serif;font-size:29px;font-weight:500;display:flex;align-items:center;padding-left:16px}

.intro{position:absolute;left:0;top:692px;width:1200px;height:91px;background:linear-gradient(#fff,#f1f1f1);text-align:center;font-size:18px;line-height:34px;padding-top:10px;color:#222}

/* how it works */
.how{position:absolute;left:0;top:783px;width:1200px;height:488px;background:linear-gradient(180deg,#dfe2e6,#f3f4f5 40%,#e1e4e8)}
.how .notch{position:absolute;left:584px;top:0;width:0;height:0;border-left:16px solid transparent;border-right:16px solid transparent;border-top:16px solid #f1f1f1}
.section-title{position:absolute;left:0;width:1200px;text-align:center;font-size:36px;font-weight:400;color:#111}
.section-title span{color:var(--blue)}
.divider{position:absolute;left:235px;width:730px;height:2px;background:linear-gradient(90deg,transparent,#c8c8c8 30%,#c8c8c8 70%,transparent)}
.divider::after{content:"";position:absolute;left:355px;top:-9px;width:20px;height:18px;background:#9a9a9a;border:4px solid #e6e8eb}
.how .lead{position:absolute;top:148px;left:0;width:1200px;text-align:center;font-size:17px;color:#333}
.how .lead b{color:var(--blue);font-weight:600}
.step{position:absolute;top:208px;width:260px;text-align:center}
.step .circle{width:124px;height:124px;margin:0 auto;border-radius:50%;background:#fff;border:6px solid #e6e6e6;box-shadow:0 3px 8px rgba(0,0,0,.15);display:flex;align-items:center;justify-content:center;position:relative}
.step .num{position:absolute;right:-6px;top:-4px;width:30px;height:30px;border-radius:50%;background:var(--blue);color:#fff;font-size:16px;font-weight:600;display:flex;align-items:center;justify-content:center;border:3px solid #fff}
.step p{font-size:14px;line-height:20px;margin-top:24px;color:#222}
.flow-arrow{position:absolute;top:255px}

/* promo band */
.promo{position:absolute;left:0;top:1271px;width:1200px;height:133px;background:linear-gradient(180deg,var(--blue-light),var(--blue) 60%,var(--blue-dark));color:#fff;text-align:center;font-size:23px;line-height:36px;padding-top:18px}
.btn-touch{position:absolute;left:431px;top:1377px;width:338px;height:56px;background:#141414;border:3px solid #fff;border-radius:28px;color:#fff;font-size:24px;font-weight:600;display:flex;align-items:center;justify-content:center;letter-spacing:.5px}

/* services */
.services .text{position:absolute;top:1570px;left:0;width:1200px;text-align:center;font-size:16px;line-height:28px;color:#222}
.service{position:absolute;top:1643px;width:341px}
.service .photo{height:192px;border:5px solid #e9e9e9;border-radius:6px}
.service h3{font-size:26px;font-weight:400;color:var(--blue);text-align:center;margin-top:28px;letter-spacing:.5px}

/* eligibility */
.eligible{position:absolute;left:0;top:1922px;width:1200px;height:281px;background:linear-gradient(90deg,#1f2d45 0%,#2f3d55 50%,#4a5566 75%,#2a3a55 100%)}
.eligible h2{position:absolute;left:78px;top:50px;font-size:36px;font-weight:700;color:#fff}
.eligible .refer{position:absolute;left:82px;top:106px;font-size:20px;color:#fff}
.tick-list{position:absolute;display:flex;flex-direction:column;gap:16px;color:#fff;font-size:17px;font-weight:600}
.tick-list li{list-style:none;display:flex;align-items:center;gap:14px}

/* support */
.support-photo{position:absolute;left:71px;top:2203px;width:305px;height:466px;background:linear-gradient(180deg,#f2f2f2,#e3e1df 40%,#2b2b2b 70%,#1a1a1a)}
.support h2{position:absolute;left:443px;top:2322px;font-size:29px;font-weight:700;line-height:38px;color:#111}
.support h2 span{color:var(--blue)}
.support-item{position:absolute;display:flex;gap:12px;font-size:16px;line-height:21px;color:#222;width:330px}
.support-item svg{flex:none;margin-top:2px}

/* footer */
.site-footer{position:absolute;left:0;top:2669px;width:1200px;height:335px;background:linear-gradient(180deg,#26282b,#17181a);color:var(--footer-text)}
.site-footer h4{position:absolute;top:50px;font-size:20px;font-weight:600;color:#fff}
.f-rule{position:absolute;top:86px;height:1px;background:#444}
.quick-links{position:absolute;left:96px;top:100px;list-style:none;font-size:13px;line-height:27px}
.quick-links li:first-child{color:var(--blue-light)}
.contact-row{position:absolute;left:303px;display:flex;gap:12px;font-size:15px;line-height:22px;color:#ddd}
.field{position:absolute;border:1px solid #5a5a5a;background:#1b1b1c;font-size:12px;color:#999;padding:6px 8px}
.btn-submit{position:absolute;left:587px;top:247px;width:80px;height:40px;background:var(--blue);color:#fff;font-size:13px;display:flex;align-items:center;justify-content:center}
.f-brand{position:absolute;left:890px;top:74px;width:240px;text-align:center;color:#ddd;font-weight:700;font-size:17px;line-height:22px}
.f-brand .mark{width:58px;height:58px;background:#ddd;margin:0 auto 16px}
.socials{position:absolute;left:928px;top:240px;display:flex;gap:6px}
.socials span{width:38px;height:38px;border-radius:50%;background:var(--blue-light);border:2px solid #fff}
.socials span:last-child{background:#d8412f}
.copyright{position:absolute;left:0;top:3004px;width:1200px;height:47px;background:var(--blue-dark);color:#fff;font-size:14px;display:flex;align-items:center;justify-content:center}
</style>
</head>
<body>

<header class="site-header">
  <div class="topbar">
    <div class="mail">
      <svg width="18" height="14" viewBox="0 0 18 14"><rect x="1" y="1" width="16" height="12" fill="none" stroke="#fff" stroke-width="1.6"/><path d="M1 1l8 7 8-7" fill="none" stroke="#fff" stroke-width="1.6"/></svg>
      hello@brightthrift.org
    </div>
    <div class="phone">
      <svg width="16" height="16" viewBox="0 0 16 16"><path d="M3 1l3 3-2 2c1 2 3 4 6 6l2-2 3 3-2 2C8 15 1 8 1 3z" fill="#fff"/></svg>
      123-555-0147
    </div>
  </div>
  <div class="brand">
    <div class="mark"></div>
    <div>
      <div class="name">BRIGHT THRIFT</div>
      <div class="sub">SUPPORTS PENSIONERS</div>
    </div>
  </div>
  <nav class="main-nav">
    <a class="active">HOME</a><a>ABOUT US</a><a>CLIENTS</a><a>PROJECTS</a><a>TRAINING</a><a>CAREER</a><a>CONTACT US</a>
  </nav>
</header>

<section class="hero" role="img" aria-label="Senior man sitting on a balcony above solar panels on a roof, looking up at the sky">
  <div class="hero-panel">
    <h1>Bright Thrift is a pioneering approach<br>by councils to support pensioner<br>households to save money</h1>
    <div class="btn-call">CALL US TODAY</div>
  </div>
</section>

<p class="intro">Bright Thrift Is A Pioneering Approach By Councils To Support Pensioner Households To &nbsp;Save Money And Take<br>Control Of Their Energy Bills By Installing Affordable, Quality Solar Systems With No Upfront Costs.</p>

<section class="how" role="img" aria-label="Faint background of rows of solar panels">
  <div class="notch"></div>
  <h2 class="section-title" style="top:44px">HOW IT <span>WORKS</span></h2>
  <div class="divider" style="top:115px"></div>
  <p class="lead">We’ve done the hard work of finding a <b>safe</b>, <b>reliable</b> and <b>quality</b> installer so pensioners don’t have to.</p>

  <div class="step" style="left:43px">
    <div class="circle"><span class="num">1</span>
      <svg width="56" height="56" viewBox="0 0 56 56" fill="none" stroke="#0b5aa8" stroke-width="3"><circle cx="28" cy="28" r="15"/><circle cx="28" cy="28" r="22" stroke-dasharray="4 4"/><path d="M28 18v10l7 5"/></svg>
    </div>
    <p>Bright Thrift Checks That Every<br>Person Gets A Solar System That<br>Pays For Itself In Energy Savings<br>From Day One</p>
  </div>
  <div class="step" style="left:322px">
    <div class="circle"><span class="num">2</span>
      <svg width="56" height="56" viewBox="0 0 56 56" fill="none" stroke="#0b5aa8" stroke-width="3"><path d="M6 28L28 9l22 19"/><path d="M12 24v24h32V24"/><rect x="18" y="30" width="8" height="8"/><rect x="30" y="30" width="8" height="8"/></svg>
    </div>
    <p>Bright Thrift Organises For The<br>Solar System To Be Installed</p>
  </div>
  <div class="step" style="left:608px">
    <div class="circle"><span class="num">3</span>
      <svg width="56" height="56" viewBox="0 0 56 56" fill="none" stroke="#0b5aa8" stroke-width="3"><circle cx="24" cy="14" r="7"/><circle cx="34" cy="22" r="7"/><path d="M6 40c8-6 16-6 22-2h10c4 0 4 5 0 5H26"/><path d="M6 48h26l16-10c3-3 0-7-4-5l-8 5"/></svg>
    </div>
    <p>Bright Thrift Supports Pensioners<br>To Understand And Get The<br>Most Out Of Solar</p>
  </div>
  <div class="step" style="left:903px">
    <div class="circle"><span class="num">4</span>
      <svg width="56" height="56" viewBox="0 0 56 56" fill="none" stroke="#0b5aa8" stroke-width="3"><rect x="8" y="18" width="34" height="24" rx="3"/><path d="M14 12h30a4 4 0 0 1 4 4v20"/><path d="M8 26h34"/><path d="M14 36h10"/></svg>
    </div>
    <p>Pensioners Gradually Pay For<br>Cost Through Their Usual Rates<br>Payments At 0% Interest</p>
  </div>

  <svg class="flow-arrow" style="left:258px" width="120" height="30" viewBox="0 0 120 30"><path d="M4 10q56 26 108 0" fill="none" stroke="#666" stroke-width="2" stroke-dasharray="5 4"/><path d="M106 6l8 4-7 6" fill="none" stroke="#666" stroke-width="2"/></svg>
  <svg class="flow-arrow" style="left:540px;top:235px" width="120" height="30" viewBox="0 0 120 30"><path d="M4 22q56 -26 108 0" fill="none" stroke="#666" stroke-width="2" stroke-dasharray="5 4"/><path d="M106 16l8 6-8 4" fill="none" stroke="#666" stroke-width="2"/></svg>
  <svg class="flow-arrow" style="left:840px" width="120" height="30" viewBox="0 0 120 30"><path d="M4 10q56 26 108 0" fill="none" stroke="#666" stroke-width="2" stroke-dasharray="5 4"/><path d="M106 6l8 4-7 6" fill="none" stroke="#666" stroke-width="2"/></svg>
</section>

<section class="promo">
  We Are The Solar Experts In The Solar Kingdom. The KSA (Saudi Arabia) Solar Market Is<br>A Promising Market With Huge Potential
</section>
<div class="btn-touch">GET IN TOUCH TODAY</div>

<section class="services">
  <h2 class="section-title" style="top:1466px">OUR <span>SERVICES</span></h2>
  <div class="divider" style="top:1540px"></div>
  <p class="text">Over 20 Victorian councils have come together with support from the Victorian State Clean Power Jobs Fund to run<br>the Bright Thrift program.</p>
  <div class="service" style="left:71px">
    <div class="photo" role="img" aria-label="Hand holding a small green island with a solar panel, wind turbines and the sun" style="background:linear-gradient(180deg,#5fb4e8 0%,#9fd3ef 45%,#6aa84a 70%,#e9d5b8 100%)"></div>
    <h3>RENEWABLE ENERGY</h3>
  </div>
  <div class="service" style="left:427px">
    <div class="photo" role="img" aria-label="Workers installing a large field of solar panels" style="background:linear-gradient(160deg,#5b78b8,#2d4a94 50%,#3f5fa8)"></div>
    <h3>PROCESS AUTOMATION</h3>
  </div>
  <div class="service" style="left:781px">
    <div class="photo" role="img" aria-label="Engineer with ear protection working on machinery" style="background:linear-gradient(135deg,#d7d9db,#9ea3a8 50%,#4f5a66)"></div>
    <h3>GENERAL ENGINEERING</h3>
  </div>
</section>

<section class="eligible" role="img" aria-label="Dim background of an installer fitting solar panels on a rooftop">
  <h2>Is My Client Eligible?</h2>
  <p class="refer">Refer clients who are:</p>
  <ul class="tick-list" style="left:85px;top:160px">
    <li><svg width="22" height="18" viewBox="0 0 22 18"><path d="M2 9l6 6L20 2" fill="none" stroke="#fff" stroke-width="3"/></svg>Homeowners</li>
    <li><svg width="22" height="18" viewBox="0 0 22 18"><path d="M2 9l6 6L20 2" fill="none" stroke="#fff" stroke-width="3"/></svg>Pension card holders</li>
  </ul>
  <ul class="tick-list" style="left:309px;top:160px">
    <li><svg width="22" height="18" viewBox="0 0 22 18"><path d="M2 9l6 6L20 2" fill="none" stroke="#fff" stroke-width="3"/></svg>Usually at home from 9am to 5pm</li>
    <li><svg width="22" height="18" viewBox="0 0 22 18"><path d="M2 9l6 6L20 2" fill="none" stroke="#fff" stroke-width="3"/></svg>Average to high electricity users (contact Bright Thrift if unsure)</li>
  </ul>
</section>

<section class="support">
  <div class="support-photo" role="img" aria-label="Smiling businesswoman in a dark jacket with arms folded"></div>
  <h2>Bright Thrift Will Support Councils To Install Solar<br><span>For Pension Card Households By:</span></h2>

  <div class="support-item" style="left:443px;top:2422px"><svg width="20" height="18" viewBox="0 0 20 18"><circle cx="8" cy="10" r="7" fill="none" stroke="#0b5aa8" stroke-width="2"/><path d="M4 9l4 4 10-11" fill="none" stroke="#0b5aa8" stroke-width="2.5"/></svg><span>Coordinating Household Promotion &amp;<br>Recruitment</span></div>
  <div class="support-item" style="left:443px;top:2488px"><svg width="20" height="18" viewBox="0 0 20 18"><circle cx="8" cy="10" r="7" fill="none" stroke="#0b5aa8" stroke-width="2"/><path d="M4 9l4 4 10-11" fill="none" stroke="#0b5aa8" stroke-width="2.5"/></svg><span>Managing The Procurement Process<br>To Contract A Solar Installer</span></div>
  <div class="support-item" style="left:443px;top:2554px"><svg width="20" height="18" viewBox="0 0 20 18"><circle cx="8" cy="10" r="7" fill="none" stroke="#0b5aa8" stroke-width="2"/><path d="M4 9l4 4 10-11" fill="none" stroke="#0b5aa8" stroke-width="2.5"/></svg><span>Securing Lower Interest Finance<br>Options For Households</span></div>
  <div class="support-item" style="left:837px;top:2422px"><svg width="20" height="18" viewBox="0 0 20 18"><circle cx="8" cy="10" r="7" fill="none" stroke="#0b5aa8" stroke-width="2"/><path d="M4 9l4 4 10-11" fill="none" stroke="#0b5aa8" stroke-width="2.5"/></svg><span>Responding To Householder<br>Enquiries</span></div>
  <div class="support-item" style="left:837px;top:2488px"><svg width="20" height="18" viewBox="0 0 20 18"><circle cx="8" cy="10" r="7" fill="none" stroke="#0b5aa8" stroke-width="2"/><path d="M4 9l4 4 10-11" fill="none" stroke="#0b5aa8" stroke-width="2.5"/></svg><span>Administering The<br>Installations</span></div>
  <div class="support-item" style="left:837px;top:2554px"><svg width="20" height="18" viewBox="0 0 20 18"><circle cx="8" cy="10" r="7" fill="none" stroke="#0b5aa8" stroke-width="2"/><path d="M4 9l4 4 10-11" fill="none" stroke="#0b5aa8" stroke-width="2.5"/></svg><span>Evaluating The<br>Project</span></div>
</section>

<footer class="site-footer">
  <h4 style="left:83px">Quick Links</h4>
  <div class="f-rule" style="left:83px;width:180px"></div>
  <ul class="quick-links">
    <li>Home</li><li>About Us</li><li>Clients</li><li>Projects</li><li>Training</li><li>Career</li><li>Contact</li>
  </ul>

  <h4 style="left:303px">Contact Details</h4>
  <div class="f-rule" style="left:303px;width:250px"></div>
  <div class="contact-row" style="top:100px">
    <svg width="14" height="20" viewBox="0 0 14 20"><path d="M7 1a6 6 0 0 1 6 6c0 5-6 12-6 12S1 12 1 7a6 6 0 0 1 6-6z" fill="#1d74c6"/><circle cx="7" cy="7" r="2.2" fill="#222"/></svg>
    <span>Bright Thrift Supports Pensioners<br><small style="font-size:13px;color:#bbb">Harbour Road District 40210<br>Kingdom of Saudi Arabia</small></span>
  </div>
  <div class="contact-row" style="top:190px">
    <svg width="14" height="16" viewBox="0 0 16 16"><path d="M3 1l3 3-2 2c1 2 3 4 6 6l2-2 3 3-2 2C8 15 1 8 1 3z" fill="#1d74c6"/></svg>
    <span>555 0142 8870</span>
  </div>
  <div class="contact-row" style="top:250px;font-size:13px">
    <svg width="16" height="12" viewBox="0 0 18 14"><rect x="1" y="1" width="16" height="12" fill="#1d74c6"/><path d="M1 1l8 7 8-7" fill="none" stroke="#222" stroke-width="1.4"/></svg>
    <span>info@northwindpower.com</span>
  </div>

  <h4 style="left:587px">Quick Inquiry</h4>
  <div class="f-rule" style="left:587px;width:280px"></div>
  <div class="field" style="left:587px;top:111px;width:136px;height:36px">Name</div>
  <div class="field" style="left:729px;top:111px;width:136px;height:36px">Phone</div>
  <div class="field" style="left:587px;top:153px;width:278px;height:84px">Message</div>
  <div class="btn-submit">SUBMIT</div>

  <div class="f-brand">
    <div class="mark"></div>
    BRIGHT THRIFT<br>SUPPORTS PENSIONERS
  </div>
  <div class="socials"><span></span><span></span><span></span><span></span></div>
</footer>
<div class="copyright">Copyright © 2016 BRIGHT THRIFT SUPPORTS PENSIONERS. All Rights Reserved.</div>

</body>
</html>
```